KVT website

Im a Specialty contractor that specializes in fireproofing. Epoxy flooring and terrazo along with poured floors and polished concrete.

We also do fire caulking.

Im the largest specialty flooring healthcare contractor in the south east.

Dane

Contractor

```html
<!DOCTYPE html>
<html lang="en">
<head>
<meta charset="utf-8">
<title>KVT — Experts in Flooring</title>
<link href="https://fonts.googleapis.com/css2?family=Open+Sans:wght@400;600;700&display=swap" rel="stylesheet">
<style>
:root{
  --header-bg:#3b3b3b;
  --header-text:#c9c9c9;
  --logo-text:#9b9b9b;
  --nav-active:#4a4a4a;
  --hero-bg:#b9c49e;
  --hero-text:#2e2e26;
  --strip-bg:#3f3f3f;
  --content-bg:#f9f3e7;
  --body-text:#2b2b2b;
  --heading-text:#2a2a2a;
  --rule:#b9b2a2;
  --button-bg:#f1f1ee;
  --button-border:#8c8c8c;
  --panel-bg:#363636;
  --panel-text:#e6e6e6;
  --footer-bg:#3a3a3a;
  --footer-text:#ffffff;
}
*{box-sizing:border-box;margin:0;padding:0}
html,body{width:1037px;height:1200px;overflow:hidden}
body{position:relative;background:var(--content-bg);font-family:"Open Sans",sans-serif;color:var(--body-text)}
.abs{position:absolute}

/* header */
.site-header{left:0;top:0;width:1037px;height:203px;background:var(--header-bg)}
.logo{left:51px;top:68px;font-size:35px;color:var(--logo-text);letter-spacing:.5px}
.tagline{right:52px;top:44px;font-size:36px;color:var(--header-text)}
.main-nav{right:52px;top:138px;display:flex;gap:0}
.main-nav a{font-size:19px;color:var(--header-text);text-decoration:none;padding:4px 10px;margin-left:0}
.main-nav a.active{background:var(--nav-active);border-radius:3px;box-shadow:inset 0 0 0 1px #555}

/* hero */
.hero{left:0;top:203px;width:1037px;height:311px;background:var(--hero-bg)}
.hero h1{position:absolute;left:51px;top:62px;font-size:24px;font-weight:600;color:var(--hero-text);text-shadow:0 1px 1px rgba(255,255,255,.4);letter-spacing:-.3px}
.hero p{position:absolute;left:51px;top:108px;width:420px;font-size:13px;line-height:18.6px;color:var(--hero-text)}
.btn{display:inline-flex;align-items:center;justify-content:center;gap:8px;background:var(--button-bg);border:1px solid var(--button-border);border-radius:4px;color:#333;font-size:12px}
.btn-about{position:absolute;left:51px;top:265px;width:132px;height:31px;font-size:14px}
.flourish{position:absolute;left:192px;top:243px;width:90px;height:62px;background:radial-gradient(ellipse at center,rgba(110,110,80,.35),rgba(110,110,80,0) 70%)}
.hero-frame{position:absolute;left:508px;top:50px;width:477px;height:212px;background:#dfe3cf;border-radius:4px;box-shadow:0 2px 8px rgba(0,0,0,.3)}
.hero-photo{position:absolute;left:8px;top:7px;width:461px;height:196px;border-radius:3px;background:linear-gradient(180deg,#e8c5a8 0%,#f3d7c0 40%,#e0b394 75%,#b08060 100%)}
.hero-caption{position:absolute;left:0;bottom:0;width:100%;height:50px;background:rgba(60,50,45,.55);color:#f4f0ea;font-size:10px;line-height:11.5px;padding:6px 10px;border-radius:0 0 3px 3px}

.strip{left:0;top:514px;width:1037px;height:44px;background:var(--strip-bg)}

/* content */
.block h2{font-size:15px;font-weight:400;color:var(--heading-text);white-space:nowrap}
.block .rule{display:block;margin-top:2px}
.block .lead{font-size:11px;font-weight:700;margin-top:14px}
.block p{font-size:10.5px;line-height:12.1px}
.block .more{position:absolute;right:0;width:85px;height:21px}
.col-text{width:278px}
.product{width:275px}
.product .thumb{position:absolute;left:0;top:38px;width:95px;height:123px}
.product .name{position:absolute;left:106px;top:34px;font-size:11px;font-weight:600}
.product p{position:absolute;left:106px;top:58px;width:165px}
.product .more{top:148px}

.newsletter{left:710px;top:965px;width:275px;height:121px;background:var(--panel-bg);border-radius:3px;color:var(--panel-text)}
.newsletter h3{position:absolute;left:26px;top:12px;font-size:15px;font-weight:400;display:flex;align-items:center;gap:8px}
.newsletter p{position:absolute;left:26px;top:36px;font-size:10.5px;line-height:12px;width:230px}
.email{position:absolute;left:14px;top:81px;width:160px;height:22px;background:#d2d2d2;border:1px solid #999;border-radius:2px;font-size:12px;font-style:italic;color:#222;padding:2px 0 0 20px}
.subscribe{position:absolute;left:187px;top:81px;width:78px;height:20px;font-size:11px}

/* footer */
.site-footer{left:0;top:1115px;width:1037px;height:85px;background:var(--footer-bg);color:var(--footer-text)}
.footer-links{position:absolute;left:51px;top:29px;display:grid;grid-template-columns:65px 80px 90px 60px;row-gap:6px;font-size:12px;font-weight:600}
.social{position:absolute;left:520px;top:30px;display:flex;gap:3px}
.social span{width:22px;height:22px;border-radius:3px;background:#8a8a8a}
.copyright{position:absolute;right:52px;top:30px;text-align:right;font-size:12px;font-weight:600;line-height:14px}
</style>
</head>
<body>

<header class="site-header abs">
  <div class="logo abs">KVT</div>
  <div class="tagline abs">Experts in Flooring</div>
  <nav class="main-nav abs">
    <a class="active">Services</a><a>Flooring</a><a>Estimate</a><a>Tiles</a><a>About Us</a><a>Contact Us</a><a>Help</a>
  </nav>
</header>

<section class="hero abs">
  <h1>Welcome to KVT...</h1>
  <p>Lorem ipsum dolor sit amet, consectetur adipisicing elit, sed do eiusmod tempor incididunt ut labore et dolore magna aliqua. Ut enim ad minim veniam, quis nostrud exercitation ullamco laboris nisi ut aliquip ex ea commodo consequat. Duis aute irure dolor in reprehenderit in voluptate velit esse cillum dolore eu fugiat nulla pariatur. Excepteur sint occaecat cupidatat non proident, sunt in culpa qui officia deserunt mollit anim id est laborum.</p>
  <div class="btn btn-about">About Us
    <svg width="18" height="18" viewBox="0 0 18 18"><circle cx="9" cy="9" r="7.5" fill="none" stroke="#333" stroke-width="1.4"/><path d="M7 5.5 L11.5 9 L7 12.5Z" fill="#333"/></svg>
  </div>
  <div class="flourish" role="img" aria-label="Decorative flourish"></div>
  <div class="hero-frame">
    <div class="hero-photo" role="img" aria-label="Photo of a finished commercial kitchen with polished flooring">
      <div class="hero-caption">Lorem ipsum dolor sit amet, consectetur adipisicing elit, sed do eiusmod tempor incididunt ut labore et dolore magna aliqua. Ut enim ad minim veniam, quis nostrud exercitation ullamco laboris nisi ut aliquip ex ea commodo consequat. Duis aute irure</div>
    </div>
  </div>
</section>

<div class="strip abs"></div>

<!-- left column -->
<section class="block col-text abs" style="left:51px;top:576px;height:180px">
  <h2>Discription</h2>
  <svg class="rule" width="120" height="8"><path d="M0 6 Q60 -2 118 6" fill="none" stroke="var(--rule)"/></svg>
  <div class="lead" style="margin-top:4px">Lorem ipsum dolor sit amet, consectetur adipisicing.</div>
  <p style="margin-top:10px">&nbsp;sed do eiusmod tempor incididunt ut labore et dolore magna aliqua. Ut enim ad minim veniam, quis nostrud exercitation ullamco laboris nisi ut aliquip ex ea commodo consequat. Duis aute irure dolor in reprehenderit in voluptate velit esse cillum dolore eu fugiat nulla pariatur. Excepteur sint occaecat cupidatat non proident, sunt in culpa qui officia deserunt mollit anim id est laborum.</p>
  <div class="btn more" style="top:158px">Read more <svg width="13" height="13" viewBox="0 0 18 18"><circle cx="9" cy="9" r="7.5" fill="none" stroke="#333" stroke-width="1.6"/><path d="M7 5.5 L11.5 9 L7 12.5Z" fill="#333"/></svg></div>
</section>

<section class="block col-text abs" style="left:51px;top:767px;height:170px">
  <h2>Quality Feature</h2>
  <svg class="rule" width="120" height="4"><line x1="0" y1="2" x2="118" y2="2" stroke="var(--rule)" stroke-dasharray="2 1"/></svg>
  <p style="margin-top:22px">Lorem ipsum dolor sit amet, consectetur adipisicing. sed do eiusmod tempor incididunt ut labore et dolore magna aliqua. Ut enim ad minim veniam, quis nostrud exercitation ullamco laboris nisi ut aliquip ex ea commodo consequat. Duis aute irure dolor in reprehenderit in voluptate velit esse cillum dolore eu fugiat nulla pariatur. Excepteur sint occaecat cupidatat non proident, sunt in culpa qui officia deserunt mollit anim id</p>
  <div class="btn more" style="top:147px">Read more <svg width="13" height="13" viewBox="0 0 18 18"><circle cx="9" cy="9" r="7.5" fill="none" stroke="#333" stroke-width="1.6"/><path d="M7 5.5 L11.5 9 L7 12.5Z" fill="#333"/></svg></div>
</section>

<section class="block col-text abs" style="left:51px;top:959px;height:150px">
  <h2>Pakage Includes</h2>
  <svg class="rule" width="124" height="4"><line x1="0" y1="2" x2="122" y2="2" stroke="var(--rule)" stroke-dasharray="2 1"/></svg>
  <p style="margin-top:6px">&nbsp;sed do eiusmod tempor incididunt ut labore et dolore magna aliqua. Ut enim ad minim veniam, quis nostrud exercitation ullamco laboris nisi ut aliquip ex ea commodo consequat. Duis aute irure dolor in reprehenderit in voluptate velit esse cillum dolore eu fugiat nulla pariatur. Excepteur sint occaecat cupidatat non proident,</p>
  <div class="btn more" style="top:116px">Read more <svg width="13" height="13" viewBox="0 0 18 18"><circle cx="9" cy="9" r="7.5" fill="none" stroke="#333" stroke-width="1.6"/><path d="M7 5.5 L11.5 9 L7 12.5Z" fill="#333"/></svg></div>
</section>

<!-- products -->
<section class="block product abs" style="left:396px;top:576px;height:180px">
  <h2 style="padding-left:8px">Featureds Products</h2>
  <svg class="rule" width="140" height="8" style="margin-left:8px"><path d="M0 6 Q70 -2 138 6" fill="none" stroke="var(--rule)"/></svg>
  <div class="thumb" role="img" aria-label="Sample of fireproofing surface" style="background:linear-gradient(135deg,#3a3a3a,#6d6d6d 50%,#2e2e2e)"></div>
  <div class="name">Fireproofing</div>
  <p style="font-weight:700">&nbsp;sed do eiusmod tempor incididunt ut labore et dolore magna aliqua. Ut enim ad minim veniam, quis nostrud exercitation ullamco laboris nisi ut aliquip ex ea commodo consequat. Duis aute irure dolor in</p>
  <div class="btn more">Read more <svg width="13" height="13" viewBox="0 0 18 18"><circle cx="9" cy="9" r="7.5" fill="none" stroke="#333" stroke-width="1.6"/><path d="M7 5.5 L11.5 9 L7 12.5Z" fill="#333"/></svg></div>
</section>

<section class="block product abs" style="left:716px;top:576px;height:180px">
  <h2 style="padding-left:8px">Featureds Products</h2>
  <svg class="rule" width="140" height="8" style="margin-left:8px"><path d="M0 6 Q70 -2 138 6" fill="none" stroke="var(--rule)"/></svg>
  <div class="thumb" role="img" aria-label="Sample of decorative artwork floor finish" style="background:linear-gradient(135deg,#efe3cc,#d9b98a 55%,#e8d6b8)"></div>
  <div class="name">Artwork</div>
  <p>&nbsp;sed do eiusmod tempor incididunt ut labore et dolore magna aliqua. Ut enim ad minim veniam, quis nostrud exercitation ullamco laboris nisi ut aliquip ex ea commodo consequat. Duis aute irure dolor in reprehenderit in</p>
  <div class="btn more">Read more <svg width="13" height="13" viewBox="0 0 18 18"><circle cx="9" cy="9" r="7.5" fill="none" stroke="#333" stroke-width="1.6"/><path d="M7 5.5 L11.5 9 L7 12.5Z" fill="#333"/></svg></div>
</section>

<section class="block product abs" style="left:396px;top:767px;height:180px">
  <h2>Featureds Products</h2>
  <svg class="rule" width="148" height="4"><line x1="0" y1="2" x2="146" y2="2" stroke="var(--rule)" stroke-dasharray="2 1"/></svg>
  <div class="thumb" role="img" aria-label="Sample of epoxy flooring" style="top:38px;background:linear-gradient(135deg,#b8735a,#d79a80 50%,#a9634c)"></div>
  <div class="name" style="top:36px">Epoxy flooring</div>
  <p>&nbsp;Ted do eiusmod tempor incididunt ut labore et dolore magna aliqua. Ut enim ad minim veniam, quis nostrud exercitation ullamco laboris nisi ut aliquip ex ea commodo consequat. Duis aute irure dolor in reprehenderit in</p>
  <div class="btn more" style="top:147px">Read more <svg width="13" height="13" viewBox="0 0 18 18"><circle cx="9" cy="9" r="7.5" fill="none" stroke="#333" stroke-width="1.6"/><path d="M7 5.5 L11.5 9 L7 12.5Z" fill="#333"/></svg></div>
</section>

<section class="block product abs" style="left:716px;top:767px;height:180px">
  <h2>Featureds Products</h2>
  <div class="thumb" role="img" aria-label="Sample of terrazzo flooring" style="top:38px;background:linear-gradient(135deg,#2f2f2f,#7a7a7a 50%,#262626)"></div>
  <div class="name" style="top:36px">Terrazo</div>
  <p>&nbsp;sed do eiusmod tempor incididunt ut labore et dolore magna aliqua. Ut enim ad minim veniam, quis nostrud exercitation ullamco laboris nisi ut aliquip ex ea commodo consequat. Duis aute irure dolor in reprehenderit in</p>
  <div class="btn more" style="top:147px">Read more <svg width="13" height="13" viewBox="0 0 18 18"><circle cx="9" cy="9" r="7.5" fill="none" stroke="#333" stroke-width="1.6"/><path d="M7 5.5 L11.5 9 L7 12.5Z" fill="#333"/></svg></div>
</section>

<aside class="newsletter abs">
  <h3>Newsletters
    <svg width="23" height="16" viewBox="0 0 23 16"><rect x="1" y="1" width="21" height="14" fill="none" stroke="#e6e6e6" stroke-width="1.3"/><path d="M1 1 L11.5 9 L22 1 M1 15 L9 7.5 M22 15 L14 7.5" fill="none" stroke="#e6e6e6" stroke-width="1.1"/></svg>
  </h3>
  <p>Subscribe to get latest updates delivereright to your inbox. We do not spam.</p>
  <div class="email">name@email.com</div>
  <div class="btn subscribe">Subscribe</div>
</aside>

<footer class="site-footer abs">
  <nav class="footer-links">
    <span>Home</span><span>Delivery</span><span>Warranty</span><span>Payment</span>
    <span>About Us</span><span>Conmtat US</span><span>Privacy Setting</span><span>Feedback</span>
  </nav>
  <div class="social" aria-label="Social links"><span></span><span></span><span></span><span></span><span></span></div>
  <div class="copyright">copyright @ 2012<br>All right reserver | Privacy Policy</div>
</footer>

</body>
</html>
```